Harbor Stone Holdings Corporate Showcase

Provide an attractive Corporate Website for a boutique Investment Company to showcase our activities and corporate interests.

Our Company works across a number of Sectors including

Real Estate
E-Commerce
Healthcare
Beauty & Personal Care
Technology
Resources

Lets keep the personality

Modern
Global
Sophisticated
Calm
Interesting

Lets keep the pages with MINIMAL Words
Lets use Photos/ Imagery to tell the story

We'll need a Banner Menu -
About Us
Expertise
Global Outlook
Sectors
Management
Media
Contact Us

Many thanks
Best wishes
Simon.

Target Market(s)

Investors
Clients

Coding

Coded - Design and coding required

Number of Pages Required

5+ page

Font styles to use
Sans Serif

Colors
886aae
3176b5
00a990
f68e4d
f04a50
e667a6

Requirements
Must have
• WordPress Coding

Checkout this Website for look and feel - its cool:
www.qvx.example

Harbor Stone Partners
(Harbor Stone Holdings LLP)
London
E9 4PL
United Kingdom

www.HarborStonePartners.example
Nice to have
• Sophisticated colour palette - black/ brown/ blue/ purple/

```html
<!DOCTYPE html>
<html lang="en">
<head>
<meta charset="utf-8">
<title>Harbor Stone Holdings</title>
<link rel="stylesheet" href="https://fonts.googleapis.com/css2?family=Cinzel:wght@500;600&family=Roboto:wght@400;500&display=swap">
<style>
:root{
  --orange:#f68e4d;
  --purple:#886aae;
  --blue:#3176b5;
  --footer:#3a7bbd;
  --ink:#1d1d1d;
  --text:#5c5c5c;
  --soft:#f3f3f3;
  --white:#ffffff;
}
*{box-sizing:border-box;margin:0;padding:0}
html,body{width:1200px;height:3535px;overflow:hidden}
body{position:relative;font-family:'Roboto',sans-serif;color:var(--text);background:var(--white)}
.abs{position:absolute}
.serif{font-family:'Cinzel',serif;font-weight:600;color:var(--ink);letter-spacing:1.5px}

/* hero */
.hero{left:0;top:0;width:1200px;height:695px;background:linear-gradient(180deg,#4a86ad 0%,#2f95a6 45%,#21a08f 100%)}
.brand{display:flex;align-items:center;gap:12px;color:var(--white);font-family:'Cinzel',serif;font-weight:600;line-height:1.1;text-align:center}
.brand-mark{width:40px;height:40px;background:var(--white)}
.brand-name{font-size:19px;letter-spacing:1px}
.brand-sub{font-size:14px;letter-spacing:1.5px}
.nav{left:392px;top:36px;display:flex;gap:23px;font-size:15px;font-weight:500;color:var(--white)}
.nav .active{color:var(--orange);position:relative}
.nav .active::after{content:"";position:absolute;left:-5px;right:-5px;top:26px;height:3px;background:var(--orange)}
.hero-title{left:0;width:1200px;top:262px;text-align:center;font-family:'Cinzel',serif;font-weight:600;font-size:64px;color:var(--white);letter-spacing:2px}
.hero-text{left:250px;width:700px;top:348px;text-align:center;color:var(--white);font-size:17px;font-weight:500;line-height:26px}
.btn{display:flex;align-items:center;justify-content:center;gap:8px;background:var(--orange);color:var(--white);font-weight:500;text-transform:uppercase}
.btn svg{width:14px;height:14px}
.hero-btn{left:507px;top:428px;width:185px;height:49px;font-size:16px}
.arrow{width:36px;height:36px}

/* sectors */
.sectors{left:0;top:695px;width:1200px;height:810px;background:var(--soft)}
.eyebrow{color:var(--blue);font-size:18px;font-weight:500}
.center{text-align:center;left:0;width:1200px}
.rule{left:567px;top:853px;width:66px;height:3px;background:var(--orange)}
.card{width:312px;height:230px;background:var(--white);border-radius:6px;box-shadow:0 2px 10px rgba(0,0,0,.04);text-align:center}
.card svg{display:block;margin:24px auto 0;width:86px;height:86px}
.card h3{margin-top:17px;font-size:17px;font-weight:500;color:var(--ink)}
.card p{margin:16px auto 0;width:270px;font-size:14px;line-height:23px}

/* stories */
.story-title{font-size:34px;line-height:35px}
.story-text{width:390px;font-size:14px;line-height:26px}
.story-btn{width:155px;height:42px;font-size:14px}
.photo{display:block}
.line-v{width:2px;background:var(--orange)}
.line-h{height:2px;background:var(--orange)}

/* footer */
.footer{left:0;top:3232px;width:1200px;height:303px;background:var(--footer);color:var(--white)}
.foot-links{left:0;width:1200px;top:3370px;text-align:center;font-size:16px}
.foot-links span{margin:0 10px}
.contact{display:flex;align-items:center;gap:16px;font-size:15px}
.contact svg{width:20px;height:20px}
.social{width:42px;height:42px;border:2px solid var(--white);border-radius:50%}
.copy{right:112px;text-align:right;font-size:14px}
</style>
</head>
<body>

<!-- hero -->
<div class="abs hero" role="img" aria-label="Photo of a person climbing city stairs among rising arrows, tinted blue to teal"></div>
<div class="abs brand" style="left:106px;top:26px">
  <div class="brand-mark"></div>
  <div><div class="brand-name">HARBOR STONE</div><div class="brand-sub">HOLDINGS</div></div>
</div>
<nav class="abs nav">
  <span class="active">Home</span><span>About Us</span><span>Expertise</span><span>Global Outlook</span><span>Sectors</span><span>Management</span><span>Media</span><span>Contact Us</span>
</nav>
<h1 class="abs hero-title">HARBOR STONE</h1>
<p class="abs hero-text">Sed ut perspiciatis unde omnis iste natus error sit voluptatem accusantium doloremque laudantium,&nbsp; totam rem aperiam,</p>
<div class="abs btn hero-btn">Get Started
  <svg viewBox="0 0 14 14"><circle cx="7" cy="7" r="7" fill="#fff"/><path d="M5 4l3 3-3 3" stroke="#f68e4d" stroke-width="2" fill="none"/></svg>
</div>
<svg class="abs arrow" style="left:36px;top:360px" viewBox="0 0 36 36"><circle cx="18" cy="18" r="16.5" fill="none" stroke="#fff" stroke-width="2"/><path d="M21 11l-7 7 7 7" stroke="#fff" stroke-width="2" fill="none"/></svg>
<svg class="abs arrow" style="left:1128px;top:360px" viewBox="0 0 36 36"><circle cx="18" cy="18" r="16.5" fill="none" stroke="#fff" stroke-width="2"/><path d="M15 11l7 7-7 7" stroke="#fff" stroke-width="2" fill="none"/></svg>

<!-- sectors -->
<section class="abs sectors"></section>
<div class="abs center eyebrow" style="top:775px">Sectors</div>
<h2 class="abs center serif" style="top:800px;font-size:38px">WORKS ACROSS OF SECTORS</h2>
<div class="abs rule"></div>

<div class="abs card" style="left:111px;top:905px">
  <svg viewBox="0 0 86 86"><circle cx="43" cy="43" r="43" fill="#886aae"/><path d="M26 58V40l17-13 17 13v18H26zM37 58V46h12v12" stroke="#fff" stroke-width="2.5" fill="none"/></svg>
  <h3>Real Estate</h3><p>Lorem ipsum dolor sit amet, consectetur adipiscing elit, sed do tempor</p>
</div>
<div class="abs card" style="left:443px;top:905px">
  <svg viewBox="0 0 86 86"><circle cx="43" cy="43" r="43" fill="#886aae"/><path d="M22 30h7l6 22h22l5-16H31" stroke="#fff" stroke-width="2.5" fill="none"/><circle cx="38" cy="59" r="3" fill="#fff"/><circle cx="54" cy="59" r="3" fill="#fff"/><circle cx="46" cy="33" r="9" stroke="#fff" stroke-width="2" fill="none"/></svg>
  <h3>E-Commerce</h3><p>Lorem ipsum dolor sit amet, consectetur adipiscing elit, sed do tempor</p>
</div>
<div class="abs card" style="left:775px;top:905px">
  <svg viewBox="0 0 86 86"><circle cx="43" cy="43" r="43" fill="#886aae"/><path d="M43 44c-9-6-12-10-12-14a6 6 0 0 1 12-2 6 6 0 0 1 12 2c0 4-3 8-12 14z" stroke="#fff" stroke-width="2.5" fill="none"/><path d="M22 48l10 12h10M64 48L54 60H44" stroke="#fff" stroke-width="2.5" fill="none"/></svg>
  <h3>Healthcare</h3><p>Lorem ipsum dolor sit amet, consectetur adipiscing elit, sed do tempor</p>
</div>
<div class="abs card" style="left:111px;top:1161px">
  <svg viewBox="0 0 86 86"><circle cx="43" cy="43" r="43" fill="#886aae"/><circle cx="44" cy="38" r="13" stroke="#fff" stroke-width="2.5" fill="none"/><path d="M36 50l-6 12M52 50l4 12" stroke="#fff" stroke-width="2.5" fill="none"/></svg>
  <h3>Beauty &amp; Personal Care</h3><p>Lorem ipsum dolor sit amet, consectetur adipiscing elit, sed do tempor</p>
</div>
<div class="abs card" style="left:443px;top:1161px">
  <svg viewBox="0 0 86 86"><circle cx="43" cy="43" r="43" fill="#886aae"/><rect x="33" y="33" width="20" height="20" stroke="#fff" stroke-width="2.5" fill="none"/><path d="M38 33v-9M48 33v-9M38 53v9M48 53v9M33 38h-9M33 48h-9M53 38h9M53 48h9" stroke="#fff" stroke-width="2.5"/></svg>
  <h3>Technology</h3><p>Lorem ipsum dolor sit amet, consectetur adipiscing elit, sed do tempor</p>
</div>
<div class="abs card" style="left:775px;top:1161px">
  <svg viewBox="0 0 86 86"><circle cx="43" cy="43" r="43" fill="#886aae"/><circle cx="43" cy="32" r="8" stroke="#fff" stroke-width="2.5" fill="none"/><circle cx="30" cy="52" r="6" stroke="#fff" stroke-width="2.5" fill="none"/><rect x="46" y="46" width="14" height="14" stroke="#fff" stroke-width="2.5" fill="none"/></svg>
  <h3>Resources</h3><p>Lorem ipsum dolor sit amet, consectetur adipiscing elit, sed do tempor</p>
</div>

<!-- about -->
<div class="abs eyebrow" style="left:110px;top:1640px">About Us</div>
<h2 class="abs serif story-title" style="left:110px;top:1670px">HARBOR STONE<br>HOLDINGS</h2>
<p class="abs story-text" style="left:110px;top:1753px">Lorem ipsum dolor sit amet, consectetur adipiscing elit, sed do eiusmod tempor incididunt ut labore et dolore magna aliqua. Ut enim ad minim veniam, quis nostrud exercitation ullamco laboris nisi ut aliquip ex ea commodo consequat. Duis aute irure dolor in reprehenderit</p>
<div class="abs btn story-btn" style="left:110px;top:1906px">Learn More <svg viewBox="0 0 14 14"><circle cx="7" cy="7" r="7" fill="#fff"/><path d="M5 4l3 3-3 3" stroke="#f68e4d" stroke-width="2" fill="none"/></svg></div>
<div class="abs photo" style="left:580px;top:1755px;width:308px;height:200px;background:linear-gradient(135deg,#eeeeec,#d8cbb8)" role="img" aria-label="Photo of a bright modern dining room with pendant lamps"></div>
<div class="abs photo" style="left:888px;top:1858px;width:312px;height:220px;background:linear-gradient(135deg,#6b4a3a,#c9a68a)" role="img" aria-label="Photo of two women reviewing documents at a table"></div>
<div class="abs line-v" style="left:181px;top:1948px;height:218px"></div>
<div class="abs line-h" style="left:181px;top:2165px;width:560px"></div>
<div class="abs line-v" style="left:739px;top:2165px;height:14px"></div>

<!-- grow -->
<div class="abs eyebrow" style="left:692px;top:2180px">GROW WITH US</div>
<h2 class="abs serif story-title" style="left:690px;top:2210px">GLOBALISE YOUR BRAND</h2>
<p class="abs story-text" style="left:692px;top:2266px">Lorem ipsum dolor sit amet, consectetur adipiscing elit, sed do eiusmod tempor incididunt ut labore et dolore magna aliqua. Ut enim ad minim veniam, quis nostrud exercitation ullamco laboris nisi ut aliquip ex ea commodo consequat. Duis aute irure dolor in reprehenderit in voluptate velit esse cillum dolore eu fugiat nulla pariatur.</p>
<div class="abs btn story-btn" style="left:692px;top:2447px">Learn More <svg viewBox="0 0 14 14"><circle cx="7" cy="7" r="7" fill="#fff"/><path d="M5 4l3 3-3 3" stroke="#f68e4d" stroke-width="2" fill="none"/></svg></div>
<div class="abs photo" style="left:111px;top:2252px;width:463px;height:310px;background:linear-gradient(135deg,#9a9a98,#d9d8d5)" role="img" aria-label="Photo of an online shop shown on a desktop screen, tablet and phone"></div>
<div class="abs line-v" style="left:740px;top:2489px;height:222px"></div>
<div class="abs line-h" style="left:178px;top:2721px;width:426px"></div>
<div class="abs line-v" style="left:178px;top:2721px;height:18px"></div>

<!-- join -->
<div class="abs eyebrow" style="left:110px;top:2747px">JOIN US</div>
<h2 class="abs serif story-title" style="left:110px;top:2777px;font-size:29px">REACH YOUR INVESTMENTS</h2>
<p class="abs story-text" style="left:110px;top:2832px">Lorem ipsum dolor sit amet, consectetur adipiscing elit, sed do eiusmod tempor incididunt ut labore et dolore magna aliqua. Ut enim ad minim veniam, quis nostrud exercitation ullamco laboris nisi ut aliquip ex ea commodo consequat. Duis aute irure dolor in reprehenderit in voluptate velit esse cillum dolore eu fugiat nulla pariatur.</p>
<div class="abs btn story-btn" style="left:110px;top:3013px">Learn More <svg viewBox="0 0 14 14"><circle cx="7" cy="7" r="7" fill="#fff"/><path d="M5 4l3 3-3 3" stroke="#f68e4d" stroke-width="2" fill="none"/></svg></div>
<div class="abs photo" style="left:604px;top:2710px;width:394px;height:387px;background:linear-gradient(135deg,#ead9c5,#c8a68c)" role="img" aria-label="Photo of a woman in a beige outfit beside a potted plant"></div>

<!-- footer -->
<footer class="abs footer"></footer>
<div class="abs brand" style="left:482px;top:3285px">
  <div class="brand-mark"></div>
  <div><div class="brand-name">HARBOR STONE</div><div class="brand-sub">HOLDINGS</div></div>
</div>
<div class="abs foot-links" style="color:#fff">Home<span>|</span>About Us<span>|</span>Expertise<span>|</span>Global Outlook<span>|</span>Sectors<span>|</span>Management<span>|</span>Media<span>|</span>Contact Us</div>
<div class="abs contact" style="left:112px;top:3437px;color:#fff">
  <svg viewBox="0 0 20 20"><path d="M4 2l4 1 1 4-2 2a11 11 0 0 0 4 4l2-2 4 1 1 4-2 2C9 18 2 11 2 4z" stroke="#fff" stroke-width="1.3" fill="none"/></svg>555-010-0188</div>
<div class="abs contact" style="left:112px;top:3478px;color:#fff">
  <svg viewBox="0 0 20 20"><rect x="2" y="4" width="16" height="12" stroke="#fff" stroke-width="1.3" fill="none"/><path d="M2 5l8 6 8-6" stroke="#fff" stroke-width="1.3" fill="none"/></svg>info@harborstone.example</div>
<div class="abs social" style="left:470px;top:3445px"></div>
<div class="abs social" style="left:525px;top:3445px"></div>
<div class="abs social" style="left:580px;top:3445px"></div>
<div class="abs social" style="left:635px;top:3445px"></div>
<div class="abs social" style="left:689px;top:3445px"></div>
<div class="abs copy" style="top:3440px;color:#fff">© Copyright 2020 Harbor Stone.</div>
<div class="abs copy" style="top:3475px;color:#fff">All Rights Reserved</div>

</body>
</html>
```